TKR Engineering Pty Ltd

I have already had nox welding and fabrication cards made , my business has changed too TKR engineering Pty Ltd so I need my logo changed on the cards
one side have my logo then the other side have what we do.
front side logo and details
owner /operator : Curtis Halvorsen
email: tkr.works@examplemail.net
number: 0491537204
ABN: 52 604 381 927
ACN: 728 391 056
on back have in dot points what we do:
* structural steel erection
* precast panels
* site welding
*steel alteration & repair
* rigging & dogging
*labour hire
Contact Information for Business Card
all details in breif
Look and feel
Each slider illustrates characteristics of the customer's brand and the style your logo design should communicate.

```html
<!DOCTYPE html>
<html lang="en">
<head>
<meta charset="utf-8">
<title>TKR Engineering Pty Ltd – Business Card</title>
<link href="https://fonts.googleapis.com/css2?family=Montserrat:wght@500;600;700;800&display=swap" rel="stylesheet">
<style>
  :root {
    --backdrop: #727377;
    --navy: #14213a;
    --rust: #96443d;
    --white: #ffffff;
  }
  html, body {
    margin: 0;
    padding: 0;
    width: 1154px;
    height: 1200px;
    overflow: hidden;
    background: var(--backdrop);
    font-family: "Montserrat", sans-serif;
  }
  .canvas {
    position: relative;
    width: 1154px;
    height: 1200px;
  }
  .card {
    position: absolute;
    left: 204px;
    width: 744px;
    border-radius: 30px;
    overflow: hidden;
    background: var(--navy);
    color: var(--white);
  }
  .card--services { top: 147px; height: 425px; }
  .card--contact { top: 620px; height: 433px; }

  /* Services side */
  .brand-mark {
    position: absolute;
    left: 40px;
    top: 170px;
    width: 310px;
    text-align: center;
    font-weight: 800;
    text-transform: uppercase;
    color: var(--white);
    line-height: 1;
  }
  .brand-mark__name { font-size: 66px; letter-spacing: 2px; }
  .brand-mark__sub { font-size: 17px; letter-spacing: 0.5px; margin-top: 6px; }
  .divider {
    position: absolute;
    left: 373px;
    top: 98px;
    width: 2px;
    height: 230px;
    background: var(--white);
  }
  .services {
    position: absolute;
    left: 403px;
    top: 90px;
  }
  .services__title {
    margin: 0 0 8px;
    font-size: 26px;
    font-weight: 700;
    color: var(--rust);
    letter-spacing: 0.3px;
  }
  .services__list {
    list-style: none;
    margin: 0;
    padding: 0;
  }
  .services__list li {
    position: relative;
    padding-left: 17px;
    font-size: 21px;
    font-weight: 500;
    line-height: 35px;
  }
  .services__list li::before {
    content: "";
    position: absolute;
    left: 0;
    top: 15px;
    width: 8px;
    height: 8px;
    border-radius: 50%;
    background: var(--rust);
  }

  /* Contact side */
  .contact-bg { position: absolute; inset: 0; }
  .person {
    position: absolute;
    left: 30px;
    top: 82px;
  }
  .person__name {
    margin: 0;
    font-size: 27px;
    font-weight: 700;
    letter-spacing: 0.3px;
  }
  .person__role {
    margin: 8px 0 0;
    font-size: 22px;
    font-weight: 500;
  }
  .company-ids {
    position: absolute;
    left: 30px;
    top: 178px;
    font-size: 22px;
    font-weight: 500;
    line-height: 34px;
  }
  .company-ids p { margin: 0; }
  .contact-lines {
    position: absolute;
    left: 30px;
    top: 283px;
  }
  .contact-lines p {
    display: flex;
    align-items: center;
    margin: 0;
    height: 34px;
    font-size: 22px;
    font-weight: 500;
  }
  .contact-lines .phone { font-weight: 700; }
  .contact-lines svg { width: 20px; height: 20px; margin-right: 10px; flex: none; }
  .brand-mark--light {
    left: 420px;
    top: 168px;
    width: 300px;
    color: var(--navy);
  }
</style>
</head>
<body>
<main class="canvas">

  <section class="card card--services" aria-label="Services side">
    <div class="brand-mark">
      <div class="brand-mark__name">TKR</div>
      <div class="brand-mark__sub">Engineering Pty Ltd</div>
    </div>
    <div class="divider"></div>
    <div class="services">
      <h2 class="services__title">OUR SERVICES</h2>
      <ul class="services__list">
        <li>Structural steel erection</li>
        <li>Precast panels</li>
        <li>Site welding</li>
        <li>Steel alteration &amp; repair</li>
        <li>Rigging &amp; dogging</li>
        <li>Labour hire</li>
      </ul>
    </div>
  </section>

  <section class="card card--contact" aria-label="Contact side">
    <svg class="contact-bg" width="744" height="433" viewBox="0 0 744 433" aria-hidden="true">
      <rect width="744" height="433" fill="var(--navy)"/>
      <path d="M425 0 Q300 200 428 433 L468 433 Q360 230 432 0 Z" fill="var(--rust)"/>
      <path d="M432 0 Q345 215 472 433 L476 433 Q352 215 438 0 Z" fill="var(--white)"/>
      <path d="M474 0 Q330 215 476 433 L744 433 L744 0 Z" fill="var(--white)"/>
    </svg>

    <div class="person">
      <h1 class="person__name">CURTIS HALVORSEN</h1>
      <p class="person__role">Owner / Operator</p>
    </div>

    <div class="company-ids">
      <p>ACN: 728 391 056</p>
      <p>ABN: 52 604 381 927</p>
    </div>

    <div class="contact-lines">
      <p class="phone">
        <svg viewBox="0 0 20 20" aria-hidden="true">
          <path d="M2 7 Q2 3 10 3 Q18 3 18 7 L14 8 L13 6 Q10 5 7 6 L6 8 Z" fill="var(--rust)"/>
          <path d="M5 9 L15 9 L17 17 L3 17 Z" fill="var(--rust)"/>
        </svg>
        049-153-7204
      </p>
      <p>
        <svg viewBox="0 0 20 20" aria-hidden="true">
          <rect x="1" y="4" width="18" height="12" fill="var(--rust)"/>
          <path d="M1 4 L10 11 L19 4" fill="none" stroke="var(--navy)" stroke-width="1.5"/>
        </svg>
        tkr.works@examplemail.net
      </p>
    </div>

    <div class="brand-mark brand-mark--light">
      <div class="brand-mark__name">TKR</div>
      <div class="brand-mark__sub">Engineering Pty Ltd</div>
    </div>
  </section>

</main>
</body>
</html>
```